Business Card Design for a Handbags business

We are modernising our handbags website (see attached file for new front page) and are in need of a modern business card and a related design we can use on a small marquee at the markets, on letterhead, emails etc.

As the leather handbags we mostly import are from Italy, we want a smart modern European feel to the design. We are currently thinking about changing the name of the business from Larkmoor Handbags (see www.larkmoorhandbags.com.au) to Vintessa Handbags. Also open to other suggestions you may have that communicates the European influence and quality.

Target Market(s)

25-65 year old women (and some men)

Industry/Entity Type

Business

Contact Information for Business Card

Single or double sided - whichever creates more of an impact

Font styles to use
Serif
Sans Serif

Requirements
Must have
• Clean crisp look, slightly Italian or European look and feel to reflect where the handbags are imported from
Nice to have
• open to ideas

```html
<!DOCTYPE html>
<html lang="en">
<head>
<meta charset="utf-8">
<title>Larkmoor Handbags – Business Card</title>
<link href="https://fonts.googleapis.com/css2?family=Cinzel:wght@400&family=Josefin+Sans:wght@700&family=Open+Sans:wght@500&display=swap" rel="stylesheet">
<style>
  :root {
    --backdrop: #eeeeee;
    --card-top: #5c5c5c;
    --card-bottom: #464646;
    --band: #3c3c3c;
    --ring: #3f3f3f;
    --paper: #fbfbfb;
    --mark-dot: #e4e4e4;
    --ink: #111111;
    --light: #ffffff;
  }
  * { margin: 0; padding: 0; box-sizing: border-box; }
  html, body {
    width: 1200px; height: 1200px; overflow: hidden;
    background: var(--backdrop);
  }
  .card {
    position: absolute;
    width: 624px; height: 404px;
    overflow: hidden;
    background: linear-gradient(180deg, var(--card-top), var(--card-bottom));
  }
  .wordmark {
    position: absolute;
    font-family: "Cinzel", serif; font-weight: 400;
    color: var(--ink); letter-spacing: 1px; line-height: 1;
    white-space: nowrap; text-align: center;
  }
  .mark-dot {
    position: absolute; border-radius: 50%;
    background: var(--mark-dot);
  }

  /* Front */
  .card--front { left: 488px; top: 190px; }
  .front-oval {
    position: absolute; left: 34px; top: 44px;
    width: 568px; height: 317px; border-radius: 50%;
    background: var(--paper);
  }
  .card--front .mark-dot { left: 246px; top: 86px; width: 132px; height: 132px; }
  .card--front .wordmark { left: 112px; width: 400px; top: 254px; font-size: 52px; }

  /* Back */
  .card--back { left: 154px; top: 646px; }
  .back-ring {
    position: absolute; left: 334px; top: 34px;
    width: 640px; height: 640px; border-radius: 50%;
    background: var(--ring);
  }
  .back-disc {
    position: absolute; left: 342px; top: 42px;
    width: 624px; height: 624px; border-radius: 50%;
    background: var(--paper);
  }
  .card--back .mark-dot { left: 436px; top: 142px; width: 108px; height: 108px; }
  .card--back .wordmark { left: 370px; width: 248px; top: 282px; font-size: 38px; }
  .bottom-band {
    position: absolute; left: 0; bottom: 0; width: 100%; height: 38px;
    background: var(--band);
  }
  .brand-title {
    position: absolute; left: 28px; top: 70px;
    font-family: "Josefin Sans", sans-serif; font-weight: 700;
    color: var(--light); line-height: 1;
  }
  .brand-title__name { display: block; font-size: 50px; letter-spacing: -1px; }
  .brand-title__tag { display: block; font-size: 18px; margin-top: 2px; padding-left: 4px; }
  .contact-list {
    position: absolute; left: 28px; top: 196px; list-style: none;
    font-family: "Open Sans", sans-serif; font-weight: 500;
    font-size: 14px; color: var(--light);
  }
  .contact-list li {
    display: flex; align-items: center; height: 32px;
  }
  .contact-list svg { width: 30px; height: 26px; margin-right: 7px; flex: none; }
</style>
</head>
<body>

<section class="card card--front">
  <div class="front-oval"></div>
  <div class="mark-dot"></div>
  <span class="wordmark">LARKMOOR</span>
</section>

<section class="card card--back">
  <div class="back-ring"></div>
  <div class="back-disc"></div>
  <div class="mark-dot"></div>
  <span class="wordmark">LARKMOOR</span>
  <div class="bottom-band"></div>

  <h1 class="brand-title">
    <span class="brand-title__name">LARKMOOR</span>
    <span class="brand-title__tag">HANDBAGS AND ACCESSORIES</span>
  </h1>

  <ul class="contact-list">
    <li>
      <svg viewBox="0 0 30 26" aria-hidden="true"><path d="M15 2 L28 13 H24 V24 H18 V17 H12 V24 H6 V13 H2 Z" fill="#fff"/></svg>
      Marlow Heights Brisbane
    </li>
    <li>
      <svg viewBox="0 0 30 26" aria-hidden="true"><path d="M3 9 C3 3 27 3 27 9 L22 10 V7 C18 5 12 5 8 7 V10 Z" fill="#fff"/><rect x="6" y="12" width="18" height="12" rx="3" fill="#fff"/><circle cx="15" cy="18" r="3.5" fill="#4f4f4f"/></svg>
      0412 555 019
    </li>
    <li>
      <svg viewBox="0 0 30 26" aria-hidden="true"><rect x="2" y="4" width="26" height="18" fill="#fff"/><path d="M2 4 L15 15 L28 4" fill="none" stroke="#4f4f4f" stroke-width="2"/></svg>
      info@larkmoorhandbags.com.au
    </li>
    <li>
      <svg viewBox="0 0 30 26" aria-hidden="true"><g fill="none" stroke="#fff" stroke-width="1.5"><circle cx="15" cy="13" r="11"/><ellipse cx="15" cy="13" rx="5" ry="11"/><path d="M4 13 H26 M6 7 H24 M6 19 H24 M15 2 V24"/></g></svg>
      www.larkmoorhandbags.com.au
    </li>
  </ul>
</section>

</body>
</html>
```